Web Design Project

We are an IT System Integrator. We provide Norvik 500 ERP System, CRM etc. We also provide hardware, networking servicing. Please look at www.brinquot.com.sg. They provide the same service as us. We like to redesign our web site. I will attached the color that I prefer for reference.

Our website is www.ravdu.com.sg.  It has been created about 14 years ago.  We are trying to revamp it with a new look and information.   The new website must be informative, fast.    I have attached an attachment which show the color that I prefer(brownish golden).   

Our competitor (www.brinquot.com) is carrying the same trade as us.  They have all the informations In their website that we will like to have.  Therefore I recommend you to take a look at my competitor website and have a better   
understanding on the kind of information I would like to have for my new website.

This project is guarantee to the person with the best design.  We can have it guarantee.

Target Market(s)

Corporate and companies

Industry/Entity Type

Hardware

```html
<!DOCTYPE html>
<html lang="en">
<head>
<meta charset="utf-8">
<title>RVD Ravdu Information System</title>
<link rel="stylesheet" href="https://fonts.googleapis.com/css2?family=Ubuntu:wght@400;500&family=Open+Sans:wght@400;600&display=swap">
<style>
  :root {
    --brown: #8a6a20;
    --brown-dark: #765818;
    --brown-top: #a2822f;
    --gold: #a8893e;
    --gold-light: #c9a962;
    --nav-text: #7a5c14;
    --ink: #111;
    --card-label: rgba(20, 24, 28, 0.85);
    --panel-bg: #f0f1f4;
    --white: #fff;
  }
  * { box-sizing: border-box; margin: 0; padding: 0; }
  html, body { width: 1157px; height: 1200px; overflow: hidden; background: var(--white); }
  body { position: relative; font-family: "Open Sans", Arial, sans-serif; color: var(--ink); }

  .masthead { position: absolute; left: 0; top: 0; width: 1157px; height: 124px;
    background: linear-gradient(180deg, var(--brown-top) 0 24px, var(--brown) 24px 100%); }
  .search { position: absolute; left: 886px; top: 65px; width: 186px; height: 26px; border-radius: 13px;
    background: linear-gradient(180deg, #6d5215, #9a7b30); border: 1px solid #b89a52; }
  .search span { position: absolute; left: 34px; top: 4px; font: italic 13px "Open Sans", Arial, sans-serif; color: #f3ead2; }
  .search svg { position: absolute; right: 12px; top: 5px; }

  .nav-band { position: absolute; left: 0; top: 124px; width: 1157px; height: 42px; background: var(--white); }
  .nav-rule { position: absolute; left: 0; top: 166px; width: 1157px; height: 8px; background: var(--gold); }
  .nav-link { position: absolute; top: 134px; font: 400 15px "Ubuntu", Arial, sans-serif; color: var(--nav-text); letter-spacing: 0.2px; }

  .brand-tab { position: absolute; left: 464px; top: 0; width: 218px; height: 152px; }
  .brand-name { position: absolute; left: 464px; top: 46px; width: 218px; text-align: center;
    font: 500 40px "Ubuntu", Arial, sans-serif; color: var(--brown-dark); letter-spacing: 2px; }
  .brand-sub { position: absolute; left: 464px; top: 98px; width: 218px; text-align: center;
    font: 500 13px "Ubuntu", Arial, sans-serif; color: var(--brown-dark); }

  .quote { position: absolute; left: 96px; top: 192px; width: 252px; height: 350px; background: var(--brown); }
  .quote h2 { position: absolute; left: 0; top: 22px; width: 252px; text-align: center;
    font: 400 22px "Ubuntu", Arial, sans-serif; color: var(--white); }
  .quote .rule { position: absolute; left: 0; top: 57px; width: 252px; height: 2px; background: var(--white); }
  .field { position: absolute; left: 26px; width: 203px; height: 30px; background: var(--white); border: 1px solid #6b5118;
    font: 13px Arial, sans-serif; color: #111; padding: 7px 0 0 14px; }
  .send { position: absolute; left: 55px; top: 238px; width: 132px; height: 39px; border-radius: 3px;
    background: linear-gradient(180deg, #c8ab66, #9f7f37); border: 1px solid #6b5118;
    font: 400 19px "Ubuntu", Arial, sans-serif; color: var(--white); text-align: center; line-height: 37px; }

  .hero-photo { position: absolute; left: 348px; top: 192px; width: 713px; height: 350px;
    background: linear-gradient(100deg, #d9d6d2 0%, #b9aea3 30%, #e8ecef 60%, #c6d6de 100%); }
  .dots { position: absolute; left: 966px; top: 528px; display: flex; gap: 8px; }
  .dots i { width: 10px; height: 10px; border-radius: 50%; background: var(--white); display: block; }
  .dots i.on { background: #e0a030; }

  .card { position: absolute; top: 582px; width: 234px; }
  .card-photo { width: 234px; height: 136px; position: relative; }
  .card-label { position: absolute; left: 0; bottom: 2px; height: 32px; background: var(--card-label);
    font: 500 14px "Ubuntu", Arial, sans-serif; color: var(--white); padding: 7px 0 0 8px; }
  .card-label svg { position: absolute; right: 14px; top: 10px; }
  .card-rule { margin-top: 12px; height: 5px; background: var(--gold); }
  .card p { margin-top: 32px; font: 13px/19px "Open Sans", Arial, sans-serif; color: var(--ink); }

  .partners-title { position: absolute; left: 91px; top: 891px; font: 500 21px "Ubuntu", Arial, sans-serif; color: var(--ink); }
  .partners { position: absolute; left: 83px; top: 929px; width: 990px; height: 128px; background: var(--panel-bg); border: 1px solid #e2e3e7; }
  .partners-shadow { position: absolute; left: 110px; top: 1057px; width: 936px; height: 14px;
    background: radial-gradient(ellipse at top, rgba(0,0,0,0.18), transparent 70%); }
  .badge { position: absolute; top: 37px; width: 87px; height: 54px; border-radius: 6px; background: #7d7d7d;
    box-shadow: 0 2px 3px rgba(0,0,0,0.3); }
  .arrow { position: absolute; top: 46px; }

  .footer { position: absolute; left: 0; top: 1115px; width: 1157px; height: 85px; background: var(--brown); }
  .copyright { position: absolute; left: 85px; top: 34px; font: 12.5px "Open Sans", Arial, sans-serif; color: var(--white); letter-spacing: 0.3px; }
  .footer-links { position: absolute; right: 85px; top: 27px; font: 12.5px "Open Sans", Arial, sans-serif; color: var(--white); letter-spacing: 0.3px; }
  .footer-links b { font-weight: 400; margin: 0 12px; }
</style>
</head>
<body>
  <header>
    <div class="masthead"></div>
    <div class="search">
      <span>Search</span>
      <svg width="16" height="16" viewBox="0 0 16 16"><circle cx="6.5" cy="6.5" r="4.5" fill="none" stroke="#111" stroke-width="2"/><line x1="10" y1="10" x2="14" y2="14" stroke="#111" stroke-width="2.5" stroke-linecap="round"/></svg>
    </div>
    <div class="nav-band"></div>
    <div class="nav-rule"></div>
    <nav>
      <span class="nav-link" style="left:103px">SOLUTIONS</span>
      <span class="nav-link" style="left:246px">HARDWARE</span>
      <span class="nav-link" style="left:372px">SERVICES</span>
      <span class="nav-link" style="left:732px">CLIENTS</span>
      <span class="nav-link" style="left:847px">ABOUT US</span>
      <span class="nav-link" style="left:972px">CONTACT US</span>
    </nav>
    <svg class="brand-tab" viewBox="0 0 218 152">
      <defs>
        <linearGradient id="tabFill" x1="0" y1="0" x2="0" y2="1">
          <stop offset="0" stop-color="#fbf5e6"/><stop offset="0.7" stop-color="#e6d3a6"/><stop offset="1" stop-color="#b8954c"/>
        </linearGradient>
      </defs>
      <path d="M0 0 H218 V124 L109 152 L0 124 Z" fill="url(#tabFill)" stroke="#a8893e" stroke-width="1.5"/>
    </svg>
    <div class="brand-name">RVD</div>
    <div class="brand-sub">Ravdu Information System</div>
  </header>

  <section class="hero">
    <form class="quote">
      <h2>GET A QUOTE NOW!</h2>
      <div class="rule"></div>
      <div class="field" style="top:88px">Name</div>
      <div class="field" style="top:137px">Email</div>
      <div class="field" style="top:186px">Mobile no</div>
      <div class="send">SEND</div>
    </form>
    <div class="hero-photo" role="img" aria-label="Business team in a meeting room with a presenter at a flip chart"></div>
    <div class="dots"><i class="on"></i><i></i><i></i><i></i></div>
  </section>

  <section class="features">
    <article class="card" style="left:84px">
      <div class="card-photo" role="img" aria-label="Norvik certification banner" style="background:linear-gradient(135deg,#0f8a6a,#1aa37c 60%,#0c6e55)">
        <div class="card-label" style="width:186px">NORVIK CERTIFIED<svg width="8" height="12" viewBox="0 0 8 12"><path d="M1 1 L6 6 L1 11" fill="none" stroke="#fff" stroke-width="2"/></svg></div>
      </div>
      <div class="card-rule"></div>
      <p>Lorem ipsum dolor sit amet,conse adipiscing elit. Aenean at est velit. vivamus imperidiet plac.</p>
    </article>
    <article class="card" style="left:336px">
      <div class="card-photo" role="img" aria-label="Smiling businesswoman with colleagues in the background" style="background:linear-gradient(90deg,#e4e4e6,#cfc8c0 55%,#b89c86)">
        <div class="card-label" style="width:185px">SUCCESS STORIES<svg width="8" height="12" viewBox="0 0 8 12"><path d="M1 1 L6 6 L1 11" fill="none" stroke="#fff" stroke-width="2"/></svg></div>
      </div>
      <div class="card-rule"></div>
      <p>Lorem ipsum dolor sit amet,conse adipiscing elit. Aenean at est velit. vivamus imperidiet plac.</p>
    </article>
    <article class="card" style="left:588px">
      <div class="card-photo" role="img" aria-label="Hand with a pen over a financial chart" style="background:linear-gradient(135deg,#3a5f8e,#9fb9d6 50%,#e6edf5)">
        <div class="card-label" style="width:186px">LATEST KELPAC<svg width="8" height="12" viewBox="0 0 8 12"><path d="M1 1 L6 6 L1 11" fill="none" stroke="#fff" stroke-width="2"/></svg></div>
      </div>
      <div class="card-rule"></div>
      <p>Lorem ipsum dolor sit amet,conse adipiscing elit. Aenean at est velit. vivamus imperidiet plac.</p>
    </article>
    <article class="card" style="left:840px">
      <div class="card-photo" role="img" aria-label="Two businessmen in discussion" style="background:linear-gradient(90deg,#8aa0b8,#c4b3a3 50%,#a9b2bb)">
        <div class="card-label" style="width:184px">SERVICES BEYOND<svg width="8" height="12" viewBox="0 0 8 12"><path d="M1 1 L6 6 L1 11" fill="none" stroke="#fff" stroke-width="2"/></svg></div>
      </div>
      <div class="card-rule"></div>
      <p>Lorem ipsum dolor sit amet,conse adipiscing elit. Aenean at est velit. vivamus imperidiet plac.</p>
    </article>
  </section>

  <section>
    <h3 class="partners-title">OUR PARTNERS</h3>
    <div class="partners-shadow"></div>
    <div class="partners">
      <svg class="arrow" style="left:8px" width="22" height="34" viewBox="0 0 22 34"><path d="M18 2 L6 17 L18 32 L13 17 Z" fill="#c3c8d0" stroke="#9aa1ab"/></svg>
      <div class="badge" style="left:79px"></div>
      <div class="badge" style="left:258px"></div>
      <div class="badge" style="left:448px"></div>
      <div class="badge" style="left:639px"></div>
      <div class="badge" style="left:815px"></div>
      <svg class="arrow" style="left:922px" width="22" height="34" viewBox="0 0 22 34"><path d="M4 2 L16 17 L4 32 L9 17 Z" fill="#c3c8d0" stroke="#9aa1ab"/></svg>
    </div>
  </section>

  <footer class="footer">
    <div class="copyright">Copyright © RVD Ravdu information System 2012.</div>
    <div class="footer-links">Log Incident<b>|</b>Enquiry<b>|</b>Sitemap</div>
  </footer>
</body>
</html>
```